Business Card Design and stationary (thank you cards)

I am basically starting a "handyman" business but have a little ego issue with that term. I have been a professional in the design and construction business for 30 years. I want simple…I will define the scope of work I do as i move forward, and it can vary and i want it to vary.

Target Market(s)

Homeowners mostly

Industry/Entity Type

Business

Contact Information for Business Card

Company Name is "Tidy Corner Crew" Dale P. Whitcombe, 42 Larkvale Hollow Road, Ashwick, Ri, 06419 (but I may want to use a PO Box), Phone is 860-555-0187, email is dwhitcombe584@mailnest.example,

Font styles to use
Sans Serif

Requirements
Should not have
• anything pre designed….hammers or whatever…custom lines to make home features as shone but simple and elegant

```html
<!DOCTYPE html>
<html lang="en">
<head>
<meta charset="utf-8">
<title>Tidy Corner Crew – Business Card</title>
<link rel="stylesheet" href="https://fonts.googleapis.com/css2?family=Marcellus&family=PT+Sans:wght@400;700&display=swap">
<style>
  :root {
    --card-black: #000000;
    --brand-blue: #00a0c6;
    --page-white: #ffffff;
    --ink: #000000;
  }
  html, body {
    margin: 0;
    padding: 0;
    width: 1002px;
    height: 1200px;
    overflow: hidden;
    background: var(--page-white);
  }
  .canvas {
    position: relative;
    width: 1002px;
    height: 1200px;
  }
  .card {
    position: absolute;
    left: 2px;
    width: 996px;
    height: 585px;
    background: var(--card-black);
    overflow: hidden;
  }
  .card--front { top: 0; }
  .card--back { top: 612px; }
  .card__curves {
    position: absolute;
    inset: 0;
  }
  .card__curves path { fill: var(--brand-blue); }
  .brand-name {
    position: absolute;
    left: 0;
    right: 0;
    margin: 0;
    text-align: center;
    font-family: "Marcellus", serif;
    font-weight: 400;
    white-space: nowrap;
  }
  .card--front .brand-name {
    top: 236px;
    font-size: 76px;
    line-height: 90px;
    color: var(--brand-blue);
    letter-spacing: 1px;
  }
  .brand-pill {
    position: absolute;
    left: 180px;
    top: 88px;
    width: 640px;
    height: 86px;
    border-radius: 43px;
    background: var(--brand-blue);
  }
  .brand-pill .brand-name {
    top: 0;
    font-size: 62px;
    line-height: 86px;
    color: var(--ink);
  }
  .contact-panel {
    position: absolute;
    left: 0;
    top: 273px;
    width: 996px;
    height: 252px;
    border-radius: 55px;
    background: var(--brand-blue);
    font-family: "PT Sans", sans-serif;
    color: var(--ink);
    text-align: center;
  }
  .contact-panel__name {
    margin: 0;
    padding-top: 30px;
    font-size: 30px;
    font-weight: 700;
    line-height: 40px;
  }
  .contact-panel__details {
    list-style: none;
    margin: 32px 0 0;
    padding: 0;
    font-size: 24px;
    line-height: 43px;
  }
</style>
</head>
<body>
<main class="canvas">
  <section class="card card--front" aria-label="Card front">
    <svg class="card__curves" width="996" height="585" viewBox="0 0 996 585" aria-hidden="true">
      <path d="M278,0 C380,170 650,218 996,190 L996,0 Z"/>
      <path d="M0,382 C250,358 560,400 720,585 L0,585 Z"/>
    </svg>
    <h1 class="brand-name">Tidy Corner Crew</h1>
  </section>

  <section class="card card--back" aria-label="Card back">
    <div class="brand-pill">
      <p class="brand-name">Tidy Corner Crew</p>
    </div>
    <div class="contact-panel">
      <h2 class="contact-panel__name">Dale P. Whitcombe</h2>
      <ul class="contact-panel__details">
        <li>Phone : 860-555-0187</li>
        <li>email : dwhitcombe584@mailnest.example</li>
        <li>42 Larkvale Hollow Road, Ashwick, Ri, 06419</li>
      </ul>
    </div>
  </section>
</main>
</body>
</html>
```